Vell Partners Building Business Cards

We need a business card that reflects our business as "Solar Experts" in San Diego. Browse our website www.vellpartners.example our License needs to be displayed as "CSLB# 4718392" our phone number is (619) 555-0147

Save thousands on your electric bills and increase the value of your home while helping to protect the environment. Our solar installation experts will help you design the system that's right for you, using only the highest quality equipment that will look great and give you ideal performance. Our goal is to make you energy independent, and get your electric bill to 0.

Tobias Wrenfield
(619) 555-0147
tobias@vellpartners.example

Target Market(s)

Home owners in san diego looking for solar

Industry/Entity Type

Solar Energy

Contact Information for Business Card

Tobias Wrenfield
(619) 555-0147
tobias@vellpartners.example

Font styles to use
Other font styles liked:
• Use our logo font

Requirements
Must have
• License needs to be displayed as "CSLB# 4718392" our phone number is (619) 555-0147
Nice to have
• Real images of rooftop home solar in san diego
Should not have
• our business address

```html
<!DOCTYPE html>
<html lang="en">
<head>
<meta charset="utf-8">
<title>Vell Partners Building – Business Cards</title>
<link rel="stylesheet" href="https://fonts.googleapis.com/css2?family=Roboto:wght@400;500;700&display=swap">
<style>
  :root {
    --stage: #a9a6a6;
    --navy: #26407f;
    --card-blue: #2c4d96;
    --card-blue-deep: #24427f;
    --gold: #e8a721;
    --paper: #f8f8f7;
    --ink: #2a3f7a;
    --white: #ffffff;
  }
  * { box-sizing: border-box; margin: 0; padding: 0; }
  html, body {
    width: 1200px; height: 1200px; overflow: hidden;
    background: var(--stage);
    font-family: "Roboto", Arial, sans-serif;
  }
  .canvas { position: relative; width: 1200px; height: 1200px; }

  .card {
    position: absolute;
    width: 712px; height: 419px;
    border-radius: 22px;
    overflow: hidden;
  }

  /* Front */
  .card--front { left: 238px; top: 118px; background: var(--card-blue); }
  .card__photo {
    position: absolute; inset: 0;
    background: linear-gradient(160deg, #2f52a0 0%, var(--card-blue) 45%, var(--card-blue-deep) 100%);
  }
  .front__brand {
    position: absolute; left: 0; right: 0; top: 262px;
    text-align: center;
    color: var(--white);
    font-weight: 700; font-size: 50px; letter-spacing: -1px;
  }
  .front__license {
    position: absolute; left: 0; right: 0; top: 364px;
    display: flex; justify-content: center; align-items: center; gap: 20px;
    color: var(--white); font-size: 17px;
  }
  .front__rule { width: 54px; height: 3px; background: var(--gold); }

  /* Back */
  .card--back { left: 231px; top: 645px; background: var(--paper); }
  .back__brand {
    position: absolute; right: 40px; top: 40px;
    color: var(--navy);
    font-weight: 700; font-size: 38px; letter-spacing: -1px;
  }
  .contact { position: absolute; left: 41px; top: 224px; color: var(--ink); }
  .contact__name { font-weight: 700; font-size: 24px; letter-spacing: -0.3px; }
  .contact__title { font-size: 16px; margin-top: 6px; }
  .contact__list { list-style: none; margin-top: 32px; font-size: 18px; line-height: 25px; }
  .contact__list li { display: flex; align-items: center; gap: 16px; }
  .contact__icon { width: 20px; height: 16px; flex: none; }
  .accent { color: var(--gold); }
</style>
</head>
<body>
<main class="canvas">
  <section class="card card--front">
    <div class="card__photo" role="img" aria-label="Rooftop solar panels photographed from above, tinted deep blue"></div>
    <div class="front__brand">Vell Partners Building</div>
    <div class="front__license">
      <span class="front__rule"></span>
      <span>License: CSLB# 4718392</span>
      <span class="front__rule"></span>
    </div>
  </section>

  <section class="card card--back">
    <div class="back__brand">Vell Partners Building</div>
    <div class="contact">
      <h1 class="contact__name">Tobias Wrenfield</h1>
      <p class="contact__title">Managing Director</p>
      <ul class="contact__list">
        <li>
          <svg class="contact__icon" viewBox="0 0 20 16" aria-hidden="true">
            <path fill="#e8a721" d="M1 5c0-3 4-4 9-4s9 1 9 4v1h-4V4.5c-1-.6-3-.8-5-.8s-4 .2-5 .8V6H1z"/>
            <path fill="#e8a721" d="M5 7h10l3 8H2z"/>
            <circle cx="10" cy="11" r="2" fill="#f8f8f7"/>
          </svg>
          <span>(619) 555-0147</span>
        </li>
        <li>
          <svg class="contact__icon" viewBox="0 0 20 16" aria-hidden="true">
            <rect x="1" y="3" width="18" height="11" fill="#e8a721"/>
            <path d="M1 3l9 6 9-6M1 14l7-5M19 14l-7-5" stroke="#f8f8f7" stroke-width="1.3" fill="none"/>
          </svg>
          <span>tobias@<span class="accent">vellpartners</span>.example</span>
        </li>
        <li><span><span class="accent">License:</span> CSLB# 4718392</span></li>
      </ul>
    </div>
  </section>
</main>
</body>
</html>
```